Figure for presentation on a hybrid research project

We need a figure that shows a series of 6 technical projects feeding into 3 multidisciplinary hybrid projects.
The concept is a ring of 6 technical projects, which could look like a 6 colour swirl (see
https://en.lorivapedia.org/wiki/Vector_graphics for an example of a 4 colour swirl.)
The 3 hybrid projects sit in the centre because they rely on input from many of the surrounding technical projects.
I've drawn a rough version in Powerpoint - see attached file uploaded. Note, in my example I couldn't draw the swirling outer ring and the colour selection is poor. The acronym for the overall Centre using the figure is TesKARO, so we will have a mint leaf and turquoise green in the logo, plus also nerves, since we will be researching neural interconnections.
We ABSOLUTELY NEED the final form of the figure to include vector graphics formats (including a form that can be edited in Photoshop) because we may need to change the title of the technical projects or of the hybrid projects at short notice ourselves.

Target Market(s)

Academic: eminent scientists and engineers

Industry/Entity Type

Technical

Font styles to use
Sans Serif

Colors
04a990

Requirements
Must have
• The projects around the ring with all project titles legible; the final figure will be reduced to no more than 8cm x 8cm in the proposal (probably less).
• Only one colour selected, because we have included that colour in the logo that we are having designed. Otherwise, a colour series around the ring that is pleasant, and another compatible colour series for the inter 3 projects.
• We ABSOLUTELY NEED the final form of the figure to include vector graphics formats (including a form that can be edited in Photoshop) because we may need to change the title of the technical projects or of the hybrid projects at short notice ourselves.
Nice to have
• See the figure we uploaded; that's the essence
• HOWEVER VIP: two of the titles around the outer ring have changed slightly.
• Computational Modelling is now Neuronal Modelling and
• Signal Processing is now Non-Invasive Interfaces (note that I've now changed the titles on the uploaded figure)

```html
<!DOCTYPE html>
<html lang="en">
<head>
<meta charset="utf-8">
<title>Research Programme Structure</title>
<link rel="stylesheet" href="https://fonts.googleapis.com/css2?family=Arimo:wght@400&display=swap">
<style>
  :root {
    --canvas-bg: #5e5e5e;
    --petal-light: #19cdb8;
    --petal-mid: #04a990;
    --petal-deep: #04715b;
    --hub-fill: #1f7466;
    --hub-rim-light: #ffffff;
    --hub-rim-shade: #b9bec0;
    --label: #ffffff;
    --petal-edge: rgba(255, 255, 255, 0.8);
  }
  html, body {
    margin: 0;
    padding: 0;
    overflow: hidden;
    background: var(--canvas-bg);
  }
  .figure {
    width: 1200px;
    height: 1000px;
    position: relative;
    background: var(--canvas-bg);
    overflow: hidden;
  }
  .figure svg { display: block; }
  .petal {
    stroke: var(--petal-edge);
    stroke-width: 1;
  }
  .project-label {
    font-family: "Arimo", Arial, sans-serif;
    font-size: 38px;
    fill: var(--label);
    letter-spacing: 0.4px;
  }
  .hub-label {
    font-family: "Arimo", Arial, sans-serif;
    font-size: 38px;
    fill: var(--label);
  }
  .hub-divider {
    stroke: var(--label);
    stroke-width: 2.5;
  }
  .marker-dot { fill: var(--label); }
</style>
</head>
<body>
<div class="figure">
<svg width="1200" height="1000" viewBox="0 0 1200 1000" xmlns="http://www.w3.org/2000/svg">
  <defs>
    <radialGradient id="petalShade" gradientUnits="userSpaceOnUse" cx="585" cy="460" r="470">
      <stop offset="0.3" stop-color="var(--petal-deep)"/>
      <stop offset="0.6" stop-color="var(--petal-mid)"/>
      <stop offset="1" stop-color="var(--petal-light)"/>
    </radialGradient>
    <linearGradient id="hubRim" x1="0" y1="0" x2="0" y2="1">
      <stop offset="0" stop-color="var(--hub-rim-light)"/>
      <stop offset="0.6" stop-color="#e9ecec"/>
      <stop offset="1" stop-color="var(--hub-rim-shade)"/>
    </linearGradient>
    <filter id="petalShadow" x="-20%" y="-20%" width="140%" height="140%">
      <feDropShadow dx="0" dy="0" stdDeviation="7" flood-color="#00382e" flood-opacity="0.5"/>
    </filter>
    <filter id="hubShadow" x="-30%" y="-30%" width="160%" height="160%">
      <feDropShadow dx="0" dy="4" stdDeviation="14" flood-color="#00241e" flood-opacity="0.7"/>
    </filter>
    <clipPath id="livingOverlap">
      <rect x="595" y="0" width="605" height="470"/>
    </clipPath>

    <path id="arc-living" d="M 361 186 A 225 225 0 0 1 679 186"/>
    <path id="arc-gene" d="M 706 126 A 225 225 0 0 1 846 512"/>
    <path id="arc-electro" d="M 952 430 A 212 212 0 0 1 607 672"/>
    <path id="arc-optrode" d="M 429 681 A 222 222 0 0 0 761 854"/>
    <path id="arc-neuronal" d="M 325 840 A 330 330 0 0 1 360 440"/>
    <path id="arc-noninvasive" d="M 192 484 A 210 210 0 0 1 511 277"/>
  </defs>

  <g class="project-ring">
    <circle class="petal petal--living-electrode" cx="520" cy="345" r="280" fill="url(#petalShade)" filter="url(#petalShadow)"/>
    <circle class="petal petal--non-invasive" cx="400" cy="460" r="250" fill="url(#petalShade)" filter="url(#petalShadow)"/>
    <circle class="petal petal--neuronal-modelling" cx="455" cy="630" r="240" fill="url(#petalShade)" filter="url(#petalShadow)"/>
    <circle class="petal petal--optrode" cx="650" cy="665" r="245" fill="url(#petalShade)" filter="url(#petalShadow)"/>
    <circle class="petal petal--electro-modulated" cx="780" cy="525" r="245" fill="url(#petalShade)" filter="url(#petalShadow)"/>
    <circle class="petal petal--gene-regulated" cx="700" cy="345" r="255" fill="url(#petalShade)" filter="url(#petalShadow)"/>
    <g clip-path="url(#livingOverlap)">
      <circle class="petal petal--living-electrode-tuck" cx="520" cy="345" r="280" fill="url(#petalShade)" filter="url(#petalShadow)"/>
    </g>
  </g>

  <g class="project-labels">
    <text class="project-label"><textPath href="#arc-living" startOffset="50%" text-anchor="middle">Living electrode</textPath></text>
    <text class="project-label"><textPath href="#arc-gene" startOffset="50%" text-anchor="middle">Gene regulated interfaces</textPath></text>
    <text class="project-label"><textPath href="#arc-electro" startOffset="50%" text-anchor="middle">Electro-modulated interfaces</textPath></text>
    <text class="project-label"><textPath href="#arc-optrode" startOffset="50%" text-anchor="middle">Optrode interfaces</textPath></text>
    <text class="project-label"><textPath href="#arc-neuronal" startOffset="50%" text-anchor="middle">Neuronal modelling</textPath></text>
    <text class="project-label"><textPath href="#arc-noninvasive" startOffset="50%" text-anchor="middle">Non-invasiveInterfaces</textPath></text>
  </g>

  <ellipse class="marker-dot" cx="540" cy="705" rx="8" ry="10"/>

  <g class="hybrid-hub">
    <circle class="hub-rim" cx="583" cy="463" r="197" fill="url(#hubRim)" filter="url(#hubShadow)"/>
    <circle class="hub-core" cx="583" cy="463" r="183" fill="var(--hub-fill)"/>
    <line class="hub-divider" x1="583" y1="463" x2="570" y2="281"/>
    <line class="hub-divider" x1="583" y1="463" x2="750" y2="536"/>
    <line class="hub-divider" x1="583" y1="463" x2="434" y2="566"/>
    <text class="hub-label" transform="translate(490 420) rotate(-61)" text-anchor="middle" dominant-baseline="middle">Brain wiring</text>
    <text class="hub-label" transform="translate(675 405) rotate(66)" text-anchor="middle" dominant-baseline="middle">Perception</text>
    <text class="hub-label" x="598" y="566" text-anchor="middle" dominant-baseline="middle">Action</text>
  </g>
</svg>
</div>
</body>
</html>
```